PowerPoint Design Project

Hi,

Using our logo, we would like a designer to provide us with a powerpoint template that has a unique brand.

To us this means creating a color palette, treatment, a font that plays off of our logo. The color palette needs to blend well with our existing colors, but give us some options, make things "POP".

The color palette needs to include the colors (with RGB numbers), gradients, different graphic styles (solid, transparent, gradient, image fills) and lines (a callout leader line, a multi-color bar to divide content)

The palette and treatment must extend itself to graphs, charts and images.

We would also like to see different parts of our logo applied to the different template slides. For example, on a title slide we would like the image with our logo and tagline. With the end slide we would like to see our logo and URL. We also attached our logo without the tagline and also just the colored cube. So please be creative on how these are incorporated into the deck.

Images are attached.

Thank you
Carlton

Target Market(s)

Large Corporations

Requirements
Must have
• color palette, treatments and consistent fonts. color palette must complement our logo. color palette must extend to graphs, charts and images.

different logo's incorprated into the deck. For example, on a title slide we would like the image with our logo and tagline. With the end slide we would like to see our logo and URL. We also attached our logo without the tagline and also just the colored cube. So please be creative on how these are incorporated into the deck.
Should not have
• We do not want to see designers taking the logo and incorporating them into the background and calling it a template.

```html
<!DOCTYPE html>
<html lang="en">
<head>
<meta charset="utf-8">
<title>Thank You</title>
<link href="https://fonts.googleapis.com/css2?family=Carlito:wght@400;700&display=swap" rel="stylesheet">
<style>
  :root {
    --navy: #11213a;
    --title: #e4eac4;
    --title-edge: #4d5a3a;
    --brand: #c6d8e4;
    --url: #3f91b3;
    --cube-dark: #27466f;
    --cube-blue: #3a78c4;
    --cube-green: #7fa63b;
    --cube-cyan: #19a9dd;
  }
  html, body {
    margin: 0;
    padding: 0;
    overflow: hidden;
    background: var(--navy);
  }
  .slide {
    position: relative;
    width: 1200px;
    height: 900px;
    background: var(--navy);
    overflow: hidden;
    font-family: "Carlito", "Calibri", sans-serif;
  }
  .slide-title {
    position: absolute;
    top: 440px;
    left: 0;
    width: 100%;
    margin: 0;
    text-align: center;
    font-size: 114px;
    font-weight: 400;
    line-height: 1;
    color: var(--title);
    text-shadow:
      -1px -1px 0 #fbfde8,
      1px 1px 0 var(--title-edge),
      2px 2px 2px rgba(0, 0, 0, 0.6);
  }
  .brand {
    position: absolute;
    top: 728px;
    left: 0;
    width: 100%;
    text-align: center;
  }
  .brand-name {
    display: block;
    font-size: 44px;
    font-weight: 700;
    line-height: 1.1;
    color: var(--brand);
  }
  .brand-url {
    display: block;
    margin-top: 4px;
    font-size: 17px;
    font-weight: 400;
    color: var(--url);
  }
  .cube-band {
    position: absolute;
    left: 0;
    bottom: 0;
    width: 100%;
    height: 34px;
    background: linear-gradient(90deg,
      var(--cube-dark), var(--cube-blue), var(--cube-green), var(--cube-cyan),
      var(--cube-dark), var(--cube-blue), var(--cube-green), var(--cube-cyan),
      var(--cube-dark), var(--cube-blue), var(--cube-green), var(--cube-cyan));
  }
</style>
</head>
<body>
  <main class="slide">
    <h1 class="slide-title">Thank You</h1>
    <div class="brand">
      <span class="brand-name">Quillmoor Partners</span>
      <span class="brand-url">www.quillmoor.example</span>
    </div>
    <div class="cube-band" role="img" aria-label="Row of small isometric cubes in navy, blue, green and cyan"></div>
  </main>
</body>
</html>
```